Bref créative
Holiday eCard Design
postcard-sized eCard - 2012
We want to have a post card designed that will be emailed to our clients and industry contacts wishing them holiday greetings. We are looking for a holiday card that is reflective of our corporate image. Please look at our website at www.quillmarkcapital.com for an idea of our design culture. We are based in the sunny island of Bermuda, so we do not want anything reflecting a cold winter setting. I will provide examples of what we have sent in prior years to give a feel for what we are looking for.
File uploaded for a similar project done last year, we would like you to use this as a reference point.
Financial Services
This going to corporate professionals, so it should be sophisticated, yet festive. The audience is varied, so we should not be specific to Christmas, but more open to the holiday season in general.
This design will be sent via email to our clients and should be appropriately sized to fit on a single screen view of a typical email viewer. We prefer it to be approximately post card sized.
Important: Please see uploaded Zip file
Quillmark Trust logo file for use in design.
Logo of Charity that should be used in the design

```html
<!DOCTYPE html>
<html lang="en">
<head>
<meta charset="utf-8">
<title>Happy Holidays – Quillmark Trust eCard</title>
<link href="https://fonts.googleapis.com/css2?family=Pinyon+Script&family=Oswald:wght@600&family=Playfair+Display:ital,wght@1,400&family=Open+Sans:wght@400;600;700&display=swap" rel="stylesheet">
<style>
  :root {
    --frame-blue: #1c5fa3;
    --gold: #c9a24a;
    --gold-deep: #a8803a;
    --amber: #f2a81d;
    --sky-top: #bfe6f4;
    --sea: #2fb3c9;
    --sea-deep: #1491b0;
    --sand: #e4caa3;
    --sand-light: #efdcbc;
    --panel: #ffffff;
    --ink: #2a6fb0;
    --accent-teal: #2bbfb3;
    --logo-blue: #2f80c8;
    --kin-navy: #2d4f8f;
  }
  * { box-sizing: border-box; margin: 0; padding: 0; }
  html, body { width: 1200px; height: 928px; overflow: hidden; background: #ffffff; }

  .ecard {
    position: relative;
    width: 1200px;
    height: 928px;
    background: var(--frame-blue);
    padding: 20px;
  }
  .ecard__inner {
    position: relative;
    width: 100%;
    height: 100%;
    background: var(--panel);
    overflow: hidden;
  }

  .beach-scene {
    position: absolute;
    left: 0; top: 0;
    width: 1160px;
    height: 668px;
    background: linear-gradient(180deg,
      var(--sky-top) 0%,
      #8fd3e6 22%,
      var(--sea) 40%,
      var(--sea-deep) 58%,
      #7fcad0 66%,
      var(--sand-light) 72%,
      var(--sand) 100%);
  }

  .greeting {
    position: absolute;
    left: 0; right: 0; top: 52px;
    text-align: center;
  }
  .greeting__title {
    font-family: "Pinyon Script", cursive;
    font-weight: 400;
    font-size: 78px;
    line-height: 1;
    color: var(--gold);
    text-shadow: 1px 1px 0 var(--gold-deep);
  }
  .greeting__company {
    margin-top: 30px;
    font-family: "Oswald", sans-serif;
    font-weight: 600;
    font-size: 38px;
    line-height: 1;
    letter-spacing: 0.5px;
    color: var(--amber);
  }
  .greeting__wish {
    margin-top: 8px;
    font-family: "Playfair Display", serif;
    font-style: italic;
    font-size: 37px;
    line-height: 1.1;
    color: var(--amber);
  }

  .donation-panel {
    position: absolute;
    left: 0; top: 668px;
    width: 1160px;
    height: 220px;
    background: var(--panel);
    display: flex;
    align-items: center;
  }
  .brand-mark {
    display: flex;
    align-items: center;
    gap: 18px;
    margin-left: 60px;
    width: 420px;
  }
  .brand-mark__square {
    width: 74px; height: 74px;
    background: var(--logo-blue);
    flex: none;
  }
  .brand-mark__name {
    font-family: "Open Sans", sans-serif;
    font-weight: 600;
    font-size: 40px;
    line-height: 1.02;
    color: var(--logo-blue);
    text-transform: uppercase;
  }
  .donation-note {
    position: relative;
    width: 350px;
    padding-left: 26px;
    font-family: "Open Sans", sans-serif;
    font-size: 16px;
    line-height: 1.35;
    color: var(--ink);
  }
  .donation-note::before {
    content: "";
    position: absolute;
    left: 0; top: 3px;
    width: 15px; height: 15px;
    background: var(--accent-teal);
  }
  .donation-note strong { font-weight: 700; }

  .charity-mark {
    margin-left: 40px;
    display: flex;
    align-items: center;
    gap: 10px;
  }
  .charity-mark__name {
    font-family: "Open Sans", sans-serif;
    font-weight: 700;
    font-size: 30px;
    color: var(--kin-navy);
    white-space: nowrap;
  }
  .charity-mark__dot {
    width: 30px; height: 30px;
    border-radius: 50%;
    background: var(--accent-teal);
    flex: none;
  }
</style>
</head>
<body>
  <main class="ecard">
    <div class="ecard__inner">
      <div class="beach-scene" role="img" aria-label="Photograph of a sunny tropical beach with turquoise sea, silver 3D numerals 2013 standing in the sand, an orange starfish and seashells"></div>

      <header class="greeting">
        <h1 class="greeting__title">Happy Holidays</h1>
        <p class="greeting__company">THE QUILLMARK TRUST</p>
        <p class="greeting__wish">wishes you a Healthy and Prosperous New Year</p>
      </header>

      <section class="donation-panel">
        <div class="brand-mark">
          <span class="brand-mark__square"></span>
          <span class="brand-mark__name">Quillmark<br>Trust</span>
        </div>
        <p class="donation-note">
          In lieu of cards, we will make a donation to the <strong>Kinwell House</strong>, a charity that provides early intervention services to children who are suffering from family based problems such as abuse, neglect and other emotional challenges.
        </p>
        <div class="charity-mark">
          <span class="charity-mark__name">Kinwell House</span>
          <span class="charity-mark__dot"></span>
        </div>
      </section>
    </div>
  </main>
</body>
</html>
```